Morvane Locks price sheet/brochure

So I'm looking to create a pricing sheet/brochure for my hair company. The company name is "Morvane Locks" and we specialize in providing Peruvian, Brazilian and Indian weave hair. I created a logo some time ago that I'd like to use if possible. If not, I'll need to create a logo as well!

8.5 x 11....not sure how many pages are needed to properly display all pricing, but I'd like the pricing to be at a size that makes it easy for the client to read. Open A-3

Target Market(s)

Hair stylist as well as their clients. Looking to establish business in Africa as well!

Industry/Entity Type

Hair And Beauty

Font styles to use
Serif

Colors
e34298

Requirements
Must have
• Price sheet/brochure must be easy to read and give potential client all the pertinent information needed regarding our hair! Also want the brochure to present style and pride in the excellent quality hair the "Morvane Locks"! 😀
• Morvane Locks
• Base price for all hair textures. Pricing will increase depending on wave pattern.
• Peruvian & Brazilian Virgin Hair
• 4 bundle deals
• 10, 12, 14, 16 - $405
• 12, 14, 16, 18 - $434
• 14, 16, 18, 20 - $467
• 16, 18, 20, 22 - $504
• 18, 20, 22, 24 - $539
• 20, 22, 24, 26 - $576
• 22, 24, 26, 28 - $621
• 24, 26, 28, 30 - $660
• 26, 28, 30, 32 - $693
• 28, 30, 32, 34 - $728
• 30, 32, 34, 36 - $760
• 32, 34, 36, 38 - $799
• 3 bundle deals
• 10, 12, 14 - $281
• 12, 14, 16 - $333
• 14, 16, 18 - $358
• 16, 18, 20 - $385
• 18, 20, 22 - $410
• 20, 22, 24 - $432
• 22, 24, 26 - $471
• 24, 26, 28 - $500
• 26, 28, 30 - $533
• 28, 30, 32 - $560
• 30, 32, 34 - $589
• 32, 34, 36 - $608
• 34, 36, 38 - $635
• 2 Bundles
• 2 Bundles 10 - $203
• 2 Bundles 12 - $235
• 2 Bundles 14 - $251
• 2 Bundles 16 - $272
• 2 Bundles 18 - $285
• 2 Bundles 20 - $302
• 2 Bundles 22 - $346
• 2 Bundles 24 - $345
• 2 Bundles 26 - $357
• 2 Bundles 28 - $384
• 2 Bundles 30 - $418
• 2 Bundles 32 - $429
• 2 Bundles 34 - $440
• 2 Bundles 36 - $476
• 2 Bundles 38 - $502
• 1 Bundle
• 1 Bundle 10 - $97
• 1 Bundle 12 - $110
• 1 Bundle 14 - $116
• 1 Bundle 16 - $126
• 1 Bundle 18 - $134
• 1 Bundle 20 - $141
• 1 Bundle 22 - $154
• 1 Bundle 24 - $167
• 1 Bundle 26 - $172
• 1 Bundle 28 - $185
• 1 Bundle 30 - $192
• 1 Bundle 32 - $197
• 1 Bundle 34 - $205
• 1 Bundle 36 - $215
• 1 Bundle 38 - $230
• -----------------------------------------------------------------------------
• Indian Virgin Hair
• 4 bundle deals
• 10, 12, 14, 16 - $293
• 12, 14, 16, 18 - $314
• 14, 16, 18, 20 - $325
• 16, 18, 20, 22 - $348
• 18, 20, 22, 24 - $367
• 20, 22, 24, 26 - $386
• 22, 24, 26, 28 - $407
• 24, 26, 28, 30 - $425
• 26, 28, 30, 32 - $444
• 28, 30, 32, 34 - $461
• 30, 32, 34, 36 - $477
• 32, 34, 36, 38 - $495
• 3 bundle deals
• 10, 12, 14 - $223
• 12, 14, 16 - $239
• 14, 16, 18 - $252
• 16, 18, 20 - $264
• 18, 20, 22 - $278
• 20, 22, 24 - $293
• 22, 24, 26 - $308
• 24, 26, 28 - $322
• 26, 28, 30 - $337
• 28, 30, 32 - $350
• 30, 32, 34 - $262
• 32, 34, 36 - $375
• 34, 36, 38 - $390
• 2 Bundles
• 2 Bundles 10 - $74
• 2 Bundles 12 - $90
• 2 Bundles 14 - $98
• 2 Bundles 16 - $107
• 2 Bundles 18 - $115
• 2 Bundles 20 - $123
• 2 Bundles 22 - $135
• 2 Bundles 24 - $143
• 2 Bundles 26 - $154
• 2 Bundles 28 - $164
• 2 Bundles 30 - $172
• 2 Bundles 32 - $180
• 2 Bundles 34 - $189
• 2 Bundles 36 - $197
• 2 Bundles 38 - $207
• 1 Bundle
• 1 Bundle 10 - $80
• 1 Bundle 12 - $88
• 1 Bundle 14 - $93
• 1 Bundle 16 - $98
• 1 Bundle 18 - $102
• 1 Bundle 20 - $109
• 1 Bundle 22 - $115
• 1 Bundle 24 - $122
• 1 Bundle 26 - $130
• 1 Bundle 28 - $137
• 1 Bundle 30 - $144
• 1 Bundle 32 - $156
• 1 Bundle 34 - $163
• 1 Bundle 36 - $175
• 1 Bundle 38 - $190
• Hair Care
• It's very important to take good care of your hair to keep using long time, below are some brief introduction
• IMPORTANT: Treat 100% human hair extensions gently.
• 1. Wash and condition hair regularly, at maximum of 3 times a week. This will keep the moisture in from shampooing while at the same time not drying them out from over shampooing.
• 2. Combing hair gently before washing. Do not rub or twist hair.
• 3. Add mild shampoo to cool water or warm water about 35℃ (Please do not use hot water) and swish hair till clean. Rinse thoroughly.
• 4. Blot out excess water with towel and allow hair to dry naturally. Do not expose to sun
• 5. Comb curly hair gently with your fingers from end to top. Do not brush
• 6. Hair may be tangled if general care directions are not followed properly.
• Important Note:
• Brush the end of hair first, then the middle, and the top at last. DO NOT brush directly from the top and pull hard, it will break the hair. Regular care will keep the hair in good condition and avoid tangle problem, improper dyeing or other chemical process will damage the hair and cause tangle and shedding problem. Please wash the hair with warm water before proceeding dyeing.
• Details of Hair Extension Maintenance Tips
• Straight Hair:
• Maintenance
• • Shampoo at least once a week.
• • Use a shampoo no higher than pH 7.
• • Dilute one ounce of shampoo in a bowl or jug with a pint of warm water.
• • Sponge the shampoo into the hair.
• • Do not massage.
• • Rinse thoroughly.
• • Apply conditioner and comb hair, starting with the ends working your way up to your scalp.
• • Rinse thoroughly.
• • Let air-dry.
• Daily
• • Brush or comb through to style.
• • Use styling aids, such as mouse, gel, and hairspray in moderation (preferably alcohol free products).
• Sleep
• • Before going to bed, braid your hair into one loose large braid at the back of the neck.
• • After waking up, undo braid and comb through beginning at the ends and working your way up to roots.
• Natural Body Wave Hair
• Maintenance
• • Do not massage.
• • Rinse thoroughly.
• • Rinse thoroughly.
• • Let air-dry.
• • Style as desired.
• • For extra wave, hair can be set in rollers.
• Daily
• Sleep
• • After waking up, undo braid.
• • Dampen hair with a water bottle.
• • Comb through beginning at the ends and working your way up to roots.
• • Let hair air-dry.
• • Style as desired.
• For extra wave, hair can be set in rollers.
• Permed Curly and Natural Curly Hair
• Maintenance
• • Do not use oil products on permed hair, it can cause matting.
• • Do not brush or comb hair when dry, it will cause frizz and the ends may tangle.
• • Do not massage.
• • Rinse thoroughly.
• • Rinse thoroughly.
• • Scrunch up hair gently to reform curl.
• • Let air-dry.
• • Style as desired.
• Daily
• Sleep
• • Let hair air-dry.
• • Style as desired.
• Specific Conditions
• Static:
• • In colder months, you may experience some static. The best way to deal with this is to dampen your hands with water, and rub hand together so they are warm. Run the palms of your hands over your hair, without actually touching your hair. This process should help control the static.
• Swimming:
• It is not recommended that you swim with extension hair. However if you do the following precautions are recommended.
• • Never wear a swimming cap or anything that covers your hair, the friction may cause matting.
• • Before swimming comb out tangles.
• • Braid hair into one braid at back of neck.
• • Try to keep head above water.
• • Do not swim under water.
• • No diving.
• • After swimming keep head out of shower.
• • Immediately after showering undo braid, comb hair and let air-dry.
• • Follow with appropriate shampooing and conditioning as needed.
• Sauna:
• • The water of the sauna will penetrate the hair and wet it.
• • Do not wrap hair in towel, which will compress it.
• • After sauna keep head out of shower.
• Sunbathing:
• • After sunbathing do not unbraid until hair has cooled down.
• • After hair cools, undo braid, comb hair.
• Miscellaneous Tips:
• • Although the extension hair is real, it is not receiving nutrients from the scalp like your own hair. Heat is your hair extensions biggest enemy. The more you use on it, the shorter the life span of your hair. We cannot guarantee that the hair will remain silky if you use the blow dry, flat iron, or curling iron often.
• • When you sleep, we highly recommend that you braid, wrap or ponytail your hair together to prevent tangling. This will save time that would be spent untangling the hair the next morning.
• • When washing the hair, always wash it going in a downward motion. Use your fingers in a horizontal motion between wefts to clean your scalp. When rinsing, do the same to be sure that all the shampoo and conditioner residues are washed out.
• Sent from my Vorna
Nice to have
• Ditto....tried to upload logo but it was to big. Please advise!
Should not have
• Ditto....

```html
<!DOCTYPE html>
<html lang="en">
<head>
<meta charset="utf-8">
<title>Morvane Locks – Hair Price Sheet</title>
<link href="https://fonts.googleapis.com/css2?family=Tinos:wght@400;700&display=swap" rel="stylesheet">
<style>
:root{
  --pink:#ec87a4;
  --magenta:#e34298;
  --ink:#1f1d1e;
  --dark:#2b292a;
  --panel-light:#f1f1f1;
  --panel-mid:#c9c9c9;
  --paper:#e6e6e6;
  --stage:#d9d6d3;
  --white:#ffffff;
}
*{box-sizing:border-box;margin:0;padding:0}
html,body{width:1200px;height:1000px;overflow:hidden}
body{background:var(--stage);font-family:'Tinos',serif;color:var(--ink);position:relative}
.sheet{position:absolute;left:270px;width:650px;height:460px;overflow:hidden;box-shadow:0 2px 8px rgba(0,0,0,.35)}
.sheet--outside{top:18px}
.sheet--inside{top:498px;background:linear-gradient(90deg,#bfbfbf 0%,#f2f2f2 30%,#d5d5d5 50%,#f2f2f2 72%,#c4c4c4 100%)}
.abs{position:absolute}
.panel{position:absolute;top:0;height:460px;overflow:hidden}
.panel--care{left:0;width:217px;background:linear-gradient(90deg,#c8c8c8,#f4f4f4 55%,#dcdcdc)}
.panel--conditions{left:217px;width:216px;background:var(--dark);color:var(--white)}
.panel--cover{left:433px;width:217px;background:linear-gradient(180deg,#ffffff,#e8e8e8)}
.banner{position:absolute;background:var(--pink);border:1.5px solid var(--ink);text-align:center;font-weight:700;color:var(--ink);letter-spacing:.5px}
.banner--outline{border:2px solid var(--pink);background:var(--dark);color:var(--pink)}
.small{font-size:5.2px;line-height:6.2px}
.tiny{font-size:4.6px;line-height:5.6px}
.bullets{list-style:none}
.bullets li{position:relative;padding-left:5px}
.bullets li::before{content:"";position:absolute;left:0;top:2px;width:2.6px;height:2.6px;border-radius:50%;background:var(--magenta)}
.bold{font-weight:700}
.photo-circle{position:absolute;width:66px;height:66px;border-radius:50%;border:3px solid var(--ink)}
.photo-circle--dark{background:radial-gradient(circle,#4a4a4a,#141414 70%);}
.photo-circle--pink{background:radial-gradient(circle,#3a3a3a 30%,var(--pink) 75%)}
.photo-circle--light{background:radial-gradient(circle,#3a3a3a 30%,#eeeeee 75%)}
.care-step{position:absolute;left:10px;width:120px;display:flex;gap:6px}
.care-step svg{flex:0 0 20px}
.cond{position:absolute;left:8px;width:200px;display:flex;gap:6px}
.cond svg{flex:0 0 16px}
.cond h3{font-size:6.5px;color:var(--pink);font-weight:700;line-height:7px}
.cover-tag{position:absolute;left:0;right:0;bottom:0;height:23px;background:var(--dark);color:var(--pink);font-size:10px;display:flex;align-items:center;justify-content:center;gap:8px}
.cover-tag span.dot{width:4px;height:4px;border-radius:50%;background:var(--pink)}
.brand-name{position:absolute;left:14px;top:155px;font-size:19px;font-weight:700;color:var(--magenta)}
.brand-line{position:absolute;left:10px;top:190px;width:180px;font-size:4.8px;font-style:italic;color:var(--ink);border-top:2px solid var(--magenta);padding-top:1px}
.cover-title{position:absolute;left:0;right:0;top:208px;text-align:center;font-size:17px;font-weight:700}
.price-label{position:absolute;font-size:8.5px;color:#333}
.price-box{position:absolute;top:62px;height:103px;width:282px;background:var(--dark);border-radius:6px;color:var(--white)}
.price-cols{position:absolute;left:54px;top:5px;right:6px;display:grid;grid-template-columns:repeat(4,1fr);gap:4px}
.price-cols h4{font-size:4.6px;font-weight:700;text-decoration:underline;margin-bottom:1px;white-space:nowrap}
.price-cols ul{list-style:none;font-size:4.5px;line-height:5.8px;white-space:nowrap}
.price-box .photo-circle{width:42px;height:42px;left:-10px;border-width:2px;border-color:var(--white)}
.tip-col{position:absolute;top:196px}
.tip-col h3{font-size:8.5px;font-weight:400;color:#333;line-height:9px;margin-bottom:3px}
.tip-col h4{font-size:5.2px;font-weight:700;margin-top:3px}
.tip-photo{position:absolute;background:linear-gradient(180deg,#5a3a2a,#1d1514)}
</style>
</head>
<body>

<!-- Outside spread -->
<section class="sheet sheet--outside">

  <div class="panel panel--care">
    <div class="banner" style="left:16px;top:12px;width:186px;height:22px;font-size:10px;line-height:19px">HAIR CARE</div>
    <p class="abs tiny" style="left:14px;top:48px;width:190px">It's very important to take good care of your hair to keep using long time, below are some brief introduction</p>
    <p class="abs bold" style="left:14px;top:90px;width:120px;font-size:6px;line-height:7px">IMPORTANT:<br>TREAT 100% HUMAN HAIR EXTENSIONS GENTLY.</p>

    <div class="care-step tiny" style="top:124px">
      <svg width="20" height="22" viewBox="0 0 20 22"><rect x="2" y="6" width="7" height="14" rx="2" fill="var(--magenta)"/><rect x="11" y="9" width="6" height="11" rx="2" fill="#555"/><rect x="4" y="2" width="3" height="4" fill="#555"/></svg>
      <p>Wash and condition hair regularly, at maximum of 3 times a week. This will keep the moisture in from shampooing while at the same time not drying them out from over shampooing.</p>
    </div>
    <div class="care-step tiny" style="top:180px">
      <svg width="20" height="20" viewBox="0 0 20 20"><rect x="3" y="3" width="14" height="6" rx="1" fill="var(--magenta)"/><g stroke="#444" stroke-width="1"><line x1="5" y1="9" x2="5" y2="16"/><line x1="8" y1="9" x2="8" y2="16"/><line x1="11" y1="9" x2="11" y2="16"/><line x1="14" y1="9" x2="14" y2="16"/></g></svg>
      <p>Combing hair gently before washing. Do not rub or twist hair.</p>
    </div>
    <div class="care-step tiny" style="top:214px">
      <svg width="20" height="16" viewBox="0 0 20 16"><path d="M2 4h16l-2 9H4z" fill="none" stroke="#444" stroke-width="1.2"/><path d="M5 8q2.5-2 5 0t5 0" fill="none" stroke="var(--magenta)" stroke-width="1"/></svg>
      <p>Add mild shampoo to cool water or warm water about 35℃ (Please do not use hot water) and swish hair till clean. Rinse thoroughly.</p>
    </div>
    <div class="care-step tiny" style="top:262px">
      <svg width="20" height="20" viewBox="0 0 20 20"><circle cx="10" cy="10" r="4" fill="none" stroke="#444" stroke-width="1.2"/><line x1="3" y1="3" x2="17" y2="17" stroke="var(--magenta)" stroke-width="1.5"/></svg>
      <p>Blot out excess water with towel and allow hair to dry naturally. Do not expose to sun</p>
    </div>
    <div class="care-step tiny" style="top:296px">
      <svg width="20" height="20" viewBox="0 0 20 20"><line x1="4" y1="4" x2="16" y2="16" stroke="#444" stroke-width="1.5"/><line x1="16" y1="4" x2="4" y2="16" stroke="#444" stroke-width="1.5"/><circle cx="10" cy="10" r="2" fill="var(--magenta)"/></svg>
      <p>Comb curly hair gently with your fingers from end to top. Do not brush.</p>
    </div>

    <div class="photo-circle photo-circle--light" role="img" aria-label="Photo of black straight hair bundles" style="left:137px;top:82px"></div>
    <div class="photo-circle photo-circle--light" role="img" aria-label="Photo of silky straight hair bundles" style="left:137px;top:152px"></div>
    <div class="photo-circle photo-circle--pink" role="img" aria-label="Photo of body wave hair bundles" style="left:137px;top:222px"></div>
    <div class="photo-circle photo-circle--light" role="img" aria-label="Photo of loose wave hair bundles" style="left:137px;top:292px"></div>

    <p class="abs bold" style="left:14px;top:336px;width:120px;font-size:5.8px;line-height:7px">HAIR MAY BE TANGLED IF GENERAL CARE DIRECTIONS ARE NOT FOLLOWED PROPERLY.</p>
    <p class="abs bold tiny" style="left:14px;top:385px">IMPORTANT NOTE:</p>
    <ul class="abs bullets tiny" style="left:14px;top:392px;width:190px">
      <li>Brush the end of hair first, then the middle, and the top at last.</li>
      <li>DO NOT brush directly from the top and pull hard, it will break the hair.</li>
      <li>Regular care will keep the hair in good condition and avoid tangle problem, improper dyeing or other chemical process will damage the hair and cause tangle and shedding problem.</li>
      <li>Please wash the hair with warm water before proceeding dyeing.</li>
    </ul>
  </div>

  <div class="panel panel--conditions">
    <div class="banner banner--outline" style="left:14px;top:12px;width:190px;height:22px;font-size:9.5px;line-height:18px">SPECIFIC CONDITIONS</div>

    <div class="cond small" style="top:46px">
      <svg width="16" height="18" viewBox="0 0 16 18"><path d="M9 1L3 10h4l-2 7 7-10H8z" fill="var(--pink)"/></svg>
      <div><h3>STATIC</h3><p class="tiny">In colder months, you may experience some static. The best way to deal with this is to dampen your hands with water, and rub hand together so they are warm. Run the palms of your hands over your hair, without actually touching your hair. This process should help control the static.</p></div>
    </div>
    <div class="cond" style="top:98px">
      <svg width="16" height="14" viewBox="0 0 16 14"><path d="M1 6q3-3 7 0t7 0M1 11q3-3 7 0t7 0" fill="none" stroke="var(--pink)" stroke-width="1.5"/></svg>
      <div><h3>SWIMMING</h3><p class="tiny">It is not recommended that you swim with extension hair. However if you do the following precautions are recommended.</p>
      <ul class="bullets tiny">
        <li>Never wear a swimming cap or anything that covers your hair, the friction may cause matting.</li>
        <li>Before swimming comb out tangles.</li>
        <li>Braid hair into one braid at back of neck.</li>
        <li>Try to keep head above water.</li>
        <li>Do not swim under water.</li>
        <li>No diving.</li>
        <li>After swimming keep head out of shower.</li>
        <li>Immediately after showering undo braid, comb hair and let air-dry. Follow with appropriate shampooing and conditioning as needed.</li>
      </ul></div>
    </div>
    <div class="cond" style="top:216px">
      <svg width="16" height="14" viewBox="0 0 16 14"><path d="M4 8q-2-3 0-6M8 8q-2-3 0-6M12 8q-2-3 0-6" fill="none" stroke="var(--pink)" stroke-width="1.2"/><rect x="1" y="10" width="14" height="3" fill="var(--pink)"/></svg>
      <div><h3>SAUNA</h3>
      <ul class="bullets tiny">
        <li>Braid hair into one braid at back of neck.</li>
        <li>The water of the sauna will penetrate the hair and wet it.</li>
        <li>Do not wrap hair in towel, which will compress it.</li>
        <li>After sauna keep head out of shower.</li>
        <li>Immediately after showering undo braid, comb hair and let air-dry.</li>
        <li>Follow with appropriate shampooing and conditioning as needed.</li>
      </ul></div>
    </div>
    <div class="cond" style="top:292px">
      <svg width="16" height="16" viewBox="0 0 16 16"><circle cx="8" cy="8" r="3.5" fill="none" stroke="var(--pink)" stroke-width="1.2"/><g stroke="var(--pink)" stroke-width="1"><line x1="8" y1="0" x2="8" y2="3"/><line x1="8" y1="13" x2="8" y2="16"/><line x1="0" y1="8" x2="3" y2="8"/><line x1="13" y1="8" x2="16" y2="8"/><line x1="2" y1="2" x2="4" y2="4"/><line x1="12" y1="12" x2="14" y2="14"/><line x1="14" y1="2" x2="12" y2="4"/><line x1="2" y1="14" x2="4" y2="12"/></g></svg>
      <div><h3>SUNBATHING</h3>
      <ul class="bullets tiny">
        <li>Braid hair into one braid at back of neck.</li>
        <li>After sunbathing do not unbraid until hair has cooled down.</li>
        <li>After hair cools, undo braid, comb hair.</li>
        <li>Follow with appropriate shampooing and conditioning as needed.</li>
      </ul></div>
    </div>
    <div class="abs" style="left:10px;top:345px;width:198px">
      <h3 style="font-size:6.5px;color:var(--pink);font-weight:700">MISCELLANEOUS TIPS:</h3>
      <ul class="bullets tiny">
        <li>Although the extension hair is real, it is not receiving nutrients from the scalp like your own hair. Heat is your hair extensions biggest enemy. The more you use on it, the shorter the life span of your hair. We cannot guarantee that the hair will remain silky if you use the blow dry, flat iron, or curling iron often.</li>
        <li>When you sleep, we highly recommend that you braid, wrap or ponytail your hair together to prevent tangling. This will save time that would be spent untangling the hair the next morning.</li>
        <li>When washing the hair, always wash it going in a downward motion. Use your fingers in a horizontal motion between wefts to clean your scalp. When rinsing, do the same to be sure that all the shampoo and conditioner residues are washed out.</li>
      </ul>
    </div>
  </div>

  <div class="panel panel--cover">
    <svg class="abs" style="left:0;top:0" width="217" height="150" viewBox="0 0 217 150">
      <polygon points="0,0 217,0 217,150 0,40" fill="var(--dark)"/>
      <polygon points="4,4 55,4 55,50 4,40" fill="#3a3a3a" stroke="var(--white)" stroke-width="2" role="img" aria-label="Photo of straight hair bundles"/>
      <polygon points="58,4 105,4 105,70 58,54" fill="#b09070" stroke="var(--white)" stroke-width="2" role="img" aria-label="Photo of wavy hair bundles"/>
      <polygon points="108,20 158,34 158,96 108,78" fill="var(--pink)" stroke="var(--white)" stroke-width="2" role="img" aria-label="Photo of body wave hair bundles"/>
      <polygon points="161,36 213,50 213,146 161,114" fill="#e8e8e8" stroke="var(--white)" stroke-width="2" role="img" aria-label="Photo of loose wave hair bundles"/>
    </svg>
    <div class="brand-name">Morvane Locks</div>
    <p class="brand-line">Providing the ultimate in professional hair care solutions</p>
    <h1 class="cover-title">HAIR PRICE SHEET</h1>
    <div class="abs" role="img" aria-label="Photo of four women with long styled hair" style="left:0;top:238px;width:217px;height:200px;background:linear-gradient(180deg,#ececec 0%,#6b4a3a 45%,#1e1616 100%)"></div>
    <div class="cover-tag"><span>Beauty</span><span class="dot"></span><span>Excellence</span><span class="dot"></span><span>Quality</span></div>
  </div>
</section>

<!-- Inside spread -->
<section class="sheet sheet--inside">
  <div class="banner" style="left:42px;top:10px;width:566px;height:36px">
    <div style="font-size:13px;line-height:16px;margin-top:3px">BASE PRICE FOR ALL HAIR TEXTURES</div>
    <div style="font-size:6px;font-weight:400;line-height:8px">PRICING MAY INCREASE DEPENDING ON WAVE PATTERN.</div>
  </div>

  <div class="price-label" style="left:110px;top:51px">PERUVIAN &amp; BRAZILIAN VIRGIN HAIR</div>
  <div class="price-label" style="left:437px;top:51px">INDIAN VIRGIN HAIR</div>

  <div class="price-box" style="left:48px">
    <div class="photo-circle photo-circle--dark" role="img" aria-label="Photo of wavy hair bundle" style="top:6px"></div>
    <div class="photo-circle photo-circle--dark" role="img" aria-label="Photo of straight hair bundle" style="top:54px"></div>
    <div class="price-cols">
      <div><h4>4 BUNDLE DEALS</h4><ul><li>10, 12, 14, 16 – $405</li><li>12, 14, 16, 18 – $434</li><li>14, 16, 18, 20 – $467</li><li>16, 18, 20, 22 – $504</li><li>18, 20, 22, 24 – $539</li><li>20, 22, 24, 26 – $576</li><li>22, 24, 26, 28 – $621</li><li>24, 26, 28, 30 – $660</li><li>26, 28, 30, 32 – $693</li><li>28, 30, 32, 34 – $728</li><li>30, 32, 34, 36 – $760</li><li>32, 34, 36, 38 – $799</li></ul></div>
      <div><h4>3 BUNDLE DEALS</h4><ul><li>10, 12, 14 – $281</li><li>12, 14, 16 – $333</li><li>14, 16, 18 – $358</li><li>16, 18, 20 – $385</li><li>18, 20, 22 – $410</li><li>20, 22, 24 – $432</li><li>22, 24, 26 – $471</li><li>24, 26, 28 – $500</li><li>26, 28, 30 – $533</li><li>28, 30, 32 – $560</li><li>30, 32, 34 – $589</li><li>32, 34, 36 – $608</li><li>34, 36, 38 – $635</li></ul></div>
      <div><h4>2 BUNDLE DEALS</h4><ul><li>2 Bundles 10 – $203</li><li>2 Bundles 12 – $235</li><li>2 Bundles 14 – $251</li><li>2 Bundles 16 – $272</li><li>2 Bundles 18 – $285</li><li>2 Bundles 20 – $302</li><li>2 Bundles 22 – $346</li><li>2 Bundles 24 – $345</li><li>2 Bundles 26 – $357</li><li>2 Bundles 28 – $384</li><li>2 Bundles 30 – $418</li><li>2 Bundles 32 – $429</li><li>2 Bundles 34 – $440</li><li>2 Bundles 36 – $476</li><li>2 Bundles 38 – $502</li></ul></div>
      <div><h4>1 BUNDLE DEALS</h4><ul><li>1 Bundle 10 – $97</li><li>1 Bundle 12 – $110</li><li>1 Bundle 14 – $116</li><li>1 Bundle 16 – $126</li><li>1 Bundle 18 – $134</li><li>1 Bundle 20 – $141</li><li>1 Bundle 22 – $154</li><li>1 Bundle 24 – $167</li><li>1 Bundle 26 – $172</li><li>1 Bundle 28 – $185</li><li>1 Bundle 30 – $192</li><li>1 Bundle 32 – $197</li><li>1 Bundle 34 – $205</li><li>1 Bundle 36 – $215</li><li>1 Bundle 38 – $230</li></ul></div>
    </div>
  </div>

  <div class="price-box" style="left:338px">
    <div class="photo-circle photo-circle--dark" role="img" aria-label="Photo of wavy hair bundle" style="top:6px"></div>
    <div class="photo-circle photo-circle--dark" role="img" aria-label="Photo of curly hair bundle" style="top:54px"></div>
    <div class="price-cols">
      <div><h4>4 BUNDLE DEALS</h4><ul><li>10, 12, 14, 16 – $293</li><li>12, 14, 16, 18 – $314</li><li>14, 16, 18, 20 – $325</li><li>16, 18, 20, 22 – $348</li><li>18, 20, 22, 24 – $367</li><li>20, 22, 24, 26 – $386</li><li>22, 24, 26, 28 – $407</li><li>24, 26, 28, 30 – $425</li><li>26, 28, 30, 32 – $444</li><li>28, 30, 32, 34 – $461</li><li>30, 32, 34, 36 – $477</li><li>32, 34, 36, 38 – $495</li></ul></div>
      <div><h4>3 BUNDLE DEALS</h4><ul><li>10, 12, 14 – $223</li><li>12, 14, 16 – $239</li><li>14, 16, 18 – $252</li><li>16, 18, 20 – $264</li><li>18, 20, 22 – $278</li><li>20, 22, 24 – $293</li><li>22, 24, 26 – $308</li><li>24, 26, 28 – $322</li><li>26, 28, 30 – $337</li><li>28, 30, 32 – $350</li><li>30, 32, 34 – $262</li><li>32, 34, 36 – $375</li><li>34, 36, 38 – $390</li></ul></div>
      <div><h4>2 BUNDLE DEALS</h4><ul><li>2 Bundles 10 – $74</li><li>2 Bundles 12 – $90</li><li>2 Bundles 14 – $98</li><li>2 Bundles 16 – $107</li><li>2 Bundles 18 – $115</li><li>2 Bundles 20 – $123</li><li>2 Bundles 22 – $135</li><li>2 Bundles 24 – $143</li><li>2 Bundles 26 – $154</li><li>2 Bundles 28 – $164</li><li>2 Bundles 30 – $172</li><li>2 Bundles 32 – $180</li><li>2 Bundles 34 – $189</li><li>2 Bundles 36 – $197</li><li>2 Bundles 38 – $207</li></ul></div>
      <div><h4>1 BUNDLE DEALS</h4><ul><li>1 Bundle 10 – $80</li><li>1 Bundle 12 – $88</li><li>1 Bundle 14 – $93</li><li>1 Bundle 16 – $98</li><li>1 Bundle 18 – $102</li><li>1 Bundle 20 – $109</li><li>1 Bundle 22 – $115</li><li>1 Bundle 24 – $122</li><li>1 Bundle 26 – $130</li><li>1 Bundle 28 – $137</li><li>1 Bundle 30 – $144</li><li>1 Bundle 32 – $156</li><li>1 Bundle 34 – $163</li><li>1 Bundle 36 – $175</li><li>1 Bundle 38 – $190</li></ul></div>
    </div>
  </div>

  <div class="banner" style="left:42px;top:168px;width:566px;height:22px;font-size:12px;line-height:19px">DETAILS OF HAIR EXTENSION MAINTENANCE TIPS</div>

  <div class="tip-photo" role="img" aria-label="Photo of two women with long straight hair" style="left:0;top:250px;width:100px;height:210px"></div>
  <div class="tip-photo" role="img" aria-label="Photo of two women with curly hair" style="left:565px;top:268px;width:85px;height:192px;background:linear-gradient(180deg,#2a2222,#120e0e)"></div>

  <div class="tip-col tiny" style="left:100px;width:125px">
    <h3>STRAIGHT HAIR</h3>
    <h4>Maintenance</h4>
    <ul class="bullets">
      <li>Shampoo at least once a week.</li>
      <li>Use a shampoo no higher than pH 7.</li>
      <li>Dilute one ounce of shampoo in a bowl or jug with a pint of warm water.</li>
      <li>Sponge the shampoo into the hair.</li>
      <li>Do not massage.</li>
      <li>Rinse thoroughly.</li>
      <li>Apply conditioner and comb hair, starting with the ends working your way up to your scalp.</li>
      <li>Rinse thoroughly.</li>
      <li>Let air-dry.</li>
    </ul>
    <h4>Daily</h4>
    <ul class="bullets">
      <li>Brush or comb through to style.</li>
      <li>Use styling aids, such as mouse, gel, and hairspray in moderation (preferably alcohol free products).</li>
    </ul>
    <h4>Sleep</h4>
    <ul class="bullets">
      <li>Before going to bed, braid your hair into one loose large braid at the back of the neck.</li>
      <li>After waking up, undo braid and comb through beginning at the ends and working your way up to roots.</li>
    </ul>
  </div>

  <div class="tip-col tiny" style="left:240px;width:190px">
    <h3>NATURAL BODY WAVE HAIR</h3>
    <h4>Maintenance</h4>
    <ul class="bullets">
      <li>Shampoo at least once a week.</li>
      <li>Use a shampoo no higher than pH 7.</li>
      <li>Dilute one ounce of shampoo in a bowl or jug with a pint of warm water.</li>
      <li>Sponge the shampoo into the hair.</li>
      <li>Do not massage.</li>
      <li>Rinse thoroughly.</li>
      <li>Apply conditioner and comb hair, starting with the ends working your way up to your scalp.</li>
      <li>Rinse thoroughly.</li>
      <li>Let air-dry.</li>
      <li>Style as desired.</li>
      <li>For extra wave, hair can be set in rollers.</li>
    </ul>
    <h4>Daily</h4>
    <ul class="bullets">
      <li>Brush or comb through to style.</li>
      <li>Use styling aids, such as mouse, gel, and hairspray in moderation (preferably alcohol free products).</li>
    </ul>
    <h4>Sleep</h4>
    <ul class="bullets">
      <li>Before going to bed, braid your hair into one loose large braid at the back of the neck.</li>
      <li>After waking up, undo braid.</li>
      <li>Dampen hair with a water bottle.</li>
      <li>Comb through beginning at the ends and working your way up to roots.</li>
      <li>Let hair air-dry.</li>
      <li>Style as desired.</li>
      <li>For extra wave, hair can be set in rollers.</li>
    </ul>
  </div>

  <div class="tip-col tiny" style="left:444px;width:160px">
    <h3>PERMED CURLY AND<br>NATURAL CURLY HAIR</h3>
    <h4>Maintenance</h4>
    <ul class="bullets">
      <li>Do not use oil products on permed hair, it can cause matting.</li>
      <li>Do not brush or comb hair when dry, it will cause frizz and the ends may tangle.</li>
      <li>Shampoo at least once a week.</li>
      <li>Use a shampoo no higher than pH 7.</li>
      <li>Dilute one ounce of shampoo in a bowl or jug with a pint of warm water.</li>
      <li>Sponge the shampoo into the hair.</li>
      <li>Do not massage.</li>
      <li>Rinse thoroughly.</li>
      <li>Apply conditioner and comb hair, starting with the ends working your way up to your scalp.</li>
      <li>Rinse thoroughly.</li>
      <li>Scrunch up hair gently to reform curl.</li>
      <li>Let air-dry.</li>
      <li>Style as desired.</li>
    </ul>
    <div style="width:110px">
    <h4>Daily</h4>
    <ul class="bullets">
      <li>Brush or comb through to style.</li>
      <li>Use styling aids, such as mouse, gel, and hairspray in moderation (preferably alcohol free products).</li>
    </ul>
    <h4>Sleep</h4>
    <ul class="bullets">
      <li>Before going to bed, braid your hair into one loose large braid at the back of the neck.</li>
      <li>After waking up, undo braid.</li>
      <li>Dampen hair with a water bottle.</li>
      <li>Comb through beginning at the ends and working your way up to roots.</li>
      <li>Scrunch up hair gently to reform curl.</li>
      <li>Let hair air-dry.</li>
      <li>Style as desired.</li>
    </ul>
    </div>
  </div>
</section>

</body>
</html>
```